New business card for UK roofing company

We are Penwick Roofing and we need a business card design for our staff.

We offer the following services:

- New roofs
- General roof repairs
- Drone surveys
- Single ply roofing
- Steel cladding
- Asbestos removal
- Electronic leak detection

I have attached our logo. I have also attached example branding printed to our vans. The business card should fit in with the style of our branding.

The business card should have the following information;

Address:
Unit 17c Marlow Dene Farm
Marlow Dene Lane
Fenbury
RX4 9QD

Telephone: 020 7946 0312
24 Hour: 0800 471 9062

Email: tom@penwickroofing.com
Mobile: 07700900418
Name: Tom Harley
Website: www.penwickroofing.com

The business card will be printed in Spot UV, see here: https://www.printvane.com/business-cards/spot-uv/

If you need anymore info, please let me know,

```html
<!DOCTYPE html>
<html lang="en">
<head>
<meta charset="utf-8">
<title>Penwick Roofing – Business Card</title>
<link href="https://fonts.googleapis.com/css2?family=Arimo:wght@400;700&display=swap" rel="stylesheet">
<style>
  :root {
    --navy: #0f4a7b;
    --cyan: #00aedb;
    --white: #ffffff;
    --backdrop: #ababab;
  }
  html, body {
    margin: 0;
    width: 1200px;
    height: 1000px;
    overflow: hidden;
    background: var(--backdrop);
    font-family: "Arimo", Arial, sans-serif;
  }
  .canvas { position: relative; width: 1200px; height: 1000px; }
  .card {
    position: absolute;
    left: 294px;
    width: 613px;
    height: 352px;
    border-radius: 28px;
    overflow: hidden;
    filter: drop-shadow(0 18px 28px rgba(0,0,0,0.35));
  }
  .card--front { top: 136px; }
  .card--back { top: 545px; }
  .card svg { display: block; width: 613px; height: 352px; }
  .brand-name { font-weight: 700; fill: var(--navy); letter-spacing: -0.5px; }
  .tagline { font-weight: 700; fill: var(--navy); font-size: 15px; letter-spacing: 0.3px; }
  .services { font-weight: 700; fill: var(--navy); font-size: 15px; }
  .phone-main { font-weight: 700; fill: var(--cyan); font-size: 30px; letter-spacing: -0.5px; }
  .phone-24 { fill: var(--white); font-size: 20px; }
  .phone-24 .label { font-weight: 700; }
  .staff-name { font-weight: 700; fill: var(--white); font-size: 23px; }
  .contact { fill: var(--white); font-size: 16px; }
  .address { fill: var(--white); font-size: 14px; }
</style>
</head>
<body>
<div class="canvas">

  <!-- Front of card -->
  <div class="card card--front">
    <svg viewBox="0 0 613 352" xmlns="http://www.w3.org/2000/svg">
      <rect width="613" height="352" fill="var(--white)"/>
      <!-- angled bands -->
      <polygon points="0,261 613,232 613,352 0,352" fill="var(--navy)"/>
      <polygon points="0,267 613,238 613,251 0,280" fill="var(--cyan)"/>
      <!-- large decorative circle -->
      <circle cx="560" cy="230" r="150" fill="var(--cyan)" stroke="var(--white)" stroke-width="8"/>
      <circle cx="560" cy="230" r="155" fill="none" stroke="var(--navy)" stroke-width="3"/>

      <!-- brand block -->
      <circle cx="158" cy="51" r="26" fill="var(--navy)"/>
      <text class="brand-name" x="158" y="124" font-size="34" text-anchor="middle">penwickroofing</text>
      <text class="tagline" x="158" y="146" text-anchor="middle">Your local roofing experts</text>

      <text class="services" text-anchor="middle">
        <tspan x="158" y="173">New roofs • General roof repairs</tspan>
        <tspan x="158" y="191">Drone surveys • Single ply roofing</tspan>
        <tspan x="158" y="208">Steel cladding • Asbestos removal</tspan>
        <tspan x="158" y="225">Electronic leak detection</tspan>
      </text>

      <!-- phone icon -->
      <path d="M49 294 c2-2 4-2 5 0 l3 4 c1 2 0 3-1 4 l-2 1 c1 3 4 6 7 7 l1-2 c1-1 2-2 4-1 l4 3 c2 1 2 3 0 5 l-2 2 c-8 2-21-11-19-19z" fill="var(--cyan)"/>
      <text class="phone-main" x="68" y="312">020 7946 0312</text>
      <text class="phone-24" x="46" y="334"><tspan class="label">24 Hour:</tspan> 0800 471 9062</text>
    </svg>
  </div>

  <!-- Back of card -->
  <div class="card card--back">
    <svg viewBox="0 0 613 352" xmlns="http://www.w3.org/2000/svg">
      <rect width="613" height="352" fill="var(--navy)"/>
      <polygon points="0,257 613,228 613,241 0,270" fill="var(--cyan)"/>
      <polygon points="0,277 613,248 613,352 0,352" fill="var(--white)"/>
      <circle cx="560" cy="210" r="150" fill="var(--cyan)" stroke="var(--white)" stroke-width="8"/>
      <circle cx="560" cy="210" r="155" fill="none" stroke="var(--navy)" stroke-width="3"/>

      <text class="staff-name" x="47" y="62">Tom Harley</text>

      <!-- phone icon -->
      <path d="M48 87 c2-2 3-2 4 0 l2 3 c1 1 0 2-1 3 l-1 1 c1 2 3 4 5 5 l1-1 c1-1 2-2 3-1 l3 2 c2 1 2 2 0 4 l-1 1 c-6 2-17-9-15-17z" fill="var(--cyan)"/>
      <text class="contact" x="72" y="98">07700900418</text>
      <!-- envelope icon -->
      <rect x="47" y="111" width="16" height="12" rx="1.5" fill="var(--cyan)"/>
      <path d="M47 112 l8 6 l8 -6" fill="none" stroke="var(--navy)" stroke-width="1.5"/>
      <text class="contact" x="72" y="122">tom@penwickroofing.com</text>
      <!-- globe icon -->
      <g fill="none" stroke="var(--cyan)" stroke-width="1.4">
        <circle cx="55" cy="141" r="7"/>
        <ellipse cx="55" cy="141" rx="3" ry="7"/>
        <line x1="48" y1="141" x2="62" y2="141"/>
        <line x1="49.5" y1="137" x2="60.5" y2="137"/>
        <line x1="49.5" y1="145" x2="60.5" y2="145"/>
      </g>
      <text class="contact" x="72" y="146">penwickroofing.com</text>

      <text class="address">
        <tspan x="47" y="179">Unit 17c Marlow Dene Farm,</tspan>
        <tspan x="47" y="197">Marlow Dene Lane, Fenbury,</tspan>
        <tspan x="47" y="214">Aldcaster RX4 9QD</tspan>
      </text>

      <!-- brand block -->
      <circle cx="58" cy="305" r="15" fill="var(--navy)"/>
      <text class="brand-name" x="86" y="317" font-size="26">penwickroofing</text>
      <text class="tagline" x="153" y="334" font-size="13" text-anchor="middle" style="font-size:13px">Your local roofing experts</text>
    </svg>
  </div>

</div>
</body>
</html>
```